IT services company needs a business card designed

-2 sided business card.-Front is going to be the logo raised (3D floating effect) on a black background. Make the logos spider web shiny silver and keep the spider the same design. -Back needs to have the following information:Darrel Sotho, Managing Partner, Cell: 738-402-1954, Website: Plankhorn.com, Email: Darrel@Plankhorn.com
Target Market(s)
IT Services
Industry/Entity Type
It Company
Contact Information for Business Card
-2 sided business card.
-Front is going to be the logo raised (3D floating effect) on a black background. Make the logos spider web shiny silver and keep the spider the same design.
-Back needs to have the following information:
Darrel Sotho, Managing Partner, Cell: 738-402-1954, Website: Plankhorn.com, Email: Darrel@Plankhorn.com

```html
<!DOCTYPE html>
<html lang="en">
<head>
<meta charset="utf-8">
<title>Plankhorn Business Card</title>
<link href="https://fonts.googleapis.com/css2?family=Montserrat:wght@400;500&display=swap" rel="stylesheet">
<style>
  :root {
    --page: #ffffff;
    --frame: #8a8a8a;
    --accent: #1a96d4;
    --ink: #111111;
    --muted: #555555;
    --card-dark: #202123;
    --on-dark: #f2f2f2;
  }
  html, body {
    margin: 0;
    padding: 0;
    width: 1200px;
    height: 1200px;
    overflow: hidden;
    background: var(--page);
  }
  .sheet {
    position: relative;
    width: 1198px;
    height: 1198px;
    border: 1px solid var(--frame);
    font-family: "Montserrat", sans-serif;
  }
  .card-info .brand {
    position: absolute;
    left: 388px;
    top: 410px;
    width: 180px;
    text-align: center;
    font-size: 27px;
    font-weight: 500;
    letter-spacing: 1px;
    color: var(--ink);
    margin: 0;
  }
  .card-info .divider {
    position: absolute;
    left: 599px;
    top: 279px;
    width: 2px;
    height: 180px;
    background: var(--accent);
  }
  .card-info .name {
    position: absolute;
    left: 632px;
    top: 292px;
    margin: 0;
    font-size: 27px;
    font-weight: 500;
    color: var(--accent);
    line-height: 1;
  }
  .card-info .role {
    position: absolute;
    left: 632px;
    top: 324px;
    margin: 0;
    font-size: 17px;
    font-weight: 400;
    color: var(--muted);
    letter-spacing: 0.3px;
  }
  .contacts {
    position: absolute;
    left: 632px;
    top: 380px;
    margin: 0;
    padding: 0;
    list-style: none;
  }
  .contacts li {
    display: flex;
    align-items: center;
    height: 21.6px;
    font-size: 13.5px;
    color: var(--muted);
  }
  .contacts svg {
    width: 13px;
    height: 13px;
    margin-right: 13px;
    flex: none;
  }
  .card-cover {
    position: absolute;
    left: 310px;
    top: 666px;
    width: 580px;
    height: 332px;
    background: var(--card-dark);
    display: flex;
    align-items: center;
    justify-content: center;
  }
  .card-cover .brand {
    margin: 0;
    font-size: 34px;
    font-weight: 500;
    letter-spacing: 2px;
    color: var(--on-dark);
  }
</style>
</head>
<body>
<div class="sheet">
  <section class="card-info">
    <p class="brand">PLANKHORN</p>
    <div class="divider"></div>
    <h1 class="name">Darrel Sotho</h1>
    <p class="role">Managing Partner</p>
    <ul class="contacts">
      <li>
        <svg viewBox="0 0 13 13" aria-hidden="true"><rect x="3" y="0.7" width="7" height="11.6" rx="1.2" fill="none" stroke="#1a96d4" stroke-width="1.3"/><circle cx="6.5" cy="10.3" r="0.8" fill="#1a96d4"/></svg>
        738-402-1954
      </li>
      <li>
        <svg viewBox="0 0 13 13" aria-hidden="true"><rect x="0.5" y="2.5" width="12" height="8" fill="#1a96d4"/><path d="M0.8 2.8 6.5 7.2 12.2 2.8M0.8 10.2 5 6.2M12.2 10.2 8 6.2" fill="none" stroke="#fff" stroke-width="1"/></svg>
        Darrel@Plankhorn.com
      </li>
      <li>
        <svg viewBox="0 0 13 13" aria-hidden="true"><circle cx="6.5" cy="6.5" r="6" fill="#1a96d4"/><g fill="none" stroke="#fff" stroke-width="0.9"><ellipse cx="6.5" cy="6.5" rx="2.6" ry="6"/><path d="M0.5 6.5h12M1.5 3.5h10M1.5 9.5h10M6.5 0.5v12"/></g></svg>
        Plankhorn.com
      </li>
    </ul>
  </section>
  <section class="card-cover">
    <p class="brand">PLANKHORN</p>
  </section>
</div>
</body>
</html>
```